Harborline Dance USA's Marigoldine

Poster Design for a Full Length Ballet

HDT Studio for Movement Learning
& Harborline Dance USA

directed by Lyle & Marjorie Fenstrom
Rosa Quillmane Dorsk, Resident Choreographer

present
"Marigoldine"

May 16 & 17 2015
Pelbury Concert Rooms
555 - 318-7042
www.pelburydancetheatre.example

The logos do not have to be present
Decorative font only in the word Marigoldine

Industry/Entity Type

Education

Font styles to use
Decorative

Colors
0493ce
3277b5
886aae

```html
<!DOCTYPE html>
<html lang="en">
<head>
<meta charset="utf-8">
<title>Marigoldine — Harborline Dance USA</title>
<link href="https://fonts.googleapis.com/css2?family=Great+Vibes&family=Tinos&display=swap" rel="stylesheet">
<style>
  :root {
    --sky-deep: #3277b5;
    --sky-bright: #0493ce;
    --sky-pale: #dfe7ef;
    --ink: #886aae;
    --ink-strong: #7a559f;
    --paper: #ffffff;
    --glass: #e9eef3;
  }
  * { margin: 0; padding: 0; box-sizing: border-box; }
  html, body { width: 792px; height: 1200px; overflow: hidden; background: var(--paper); }
  .poster {
    position: relative; width: 792px; height: 1200px; overflow: hidden;
    font-family: "Tinos", "Times New Roman", serif; color: var(--ink-strong);
  }
  .sky {
    position: absolute; inset: 0;
    background:
      radial-gradient(ellipse 45% 22% at 88% 36%, rgba(4,147,206,.55), transparent 70%),
      radial-gradient(ellipse 60% 20% at 30% 42%, rgba(255,255,255,.3), transparent 70%),
      linear-gradient(180deg, #3b8ab8 0%, #6aa3c6 18%, #86aec8 35%, #7ea2bd 50%, #a7bfd2 66%, var(--sky-pale) 84%, #eef2f6 100%);
  }
  .slipper {
    position: absolute; left: 165px; top: 560px; width: 565px; height: 500px;
    border-radius: 46% 30% 12% 40% / 30% 28% 18% 60%;
    background: linear-gradient(160deg, rgba(233,238,243,.75), rgba(200,214,228,.55) 55%, rgba(233,238,243,.7));
  }
  .border-band { position: absolute; inset: 0; }
  .line { position: absolute; left: 0; right: 0; text-align: center; white-space: nowrap; }
  .presenters { top: 112px; font-size: 25px; }
  .presents { top: 168px; font-size: 25px; }
  .title {
    top: 188px; font-family: "Great Vibes", cursive; font-weight: 400;
    font-size: 132px; line-height: 1.1; color: var(--ink); letter-spacing: 2px;
  }
  .date { top: 618px; font-size: 48px; letter-spacing: 1px; }
  .venue { top: 678px; font-size: 26px; }
  .credits { position: absolute; left: 173px; top: 966px; font-size: 25px; line-height: 32px; }
  .contact { position: absolute; right: 84px; top: 1078px; text-align: right; font-size: 25px; line-height: 32px; }
  .contact .phone { margin-right: 80px; }
  .studio-mark {
    position: absolute; left: 62px; top: 1046px; width: 122px; height: 96px; background: var(--paper);
    display: flex; align-items: center; justify-content: center; gap: 5px; padding: 6px;
  }
  .studio-mark .dot { width: 12px; height: 12px; border-radius: 50%; background: var(--ink-strong); flex: none; }
  .studio-mark .name { font-size: 11px; line-height: 13px; color: var(--ink-strong); }
</style>
</head>
<body>
<main class="poster">
  <div class="sky" role="img" aria-label="Cloudy blue sky background"></div>
  <div class="slipper" role="img" aria-label="Glass slipper photographed against the sky"></div>
  <svg class="border-band" width="792" height="1200" viewBox="0 0 792 1200" role="img" aria-label="Purple swirl pattern border">
    <g fill="var(--ink)" fill-opacity="0.35">
      <rect x="56" y="22" width="680" height="28"/>
      <rect x="56" y="1150" width="680" height="28"/>
      <rect x="20" y="60" width="26" height="1080"/>
      <rect x="746" y="60" width="26" height="1080"/>
    </g>
  </svg>

  <p class="line presenters">HDT Studio for Movement Learning &amp; Harborline Dance USA</p>
  <p class="line presents">PRESENTS</p>
  <h1 class="line title">Marigoldine</h1>

  <p class="line date">MAY 16 &amp; 17 2015</p>
  <p class="line venue">at the Pelbury Concert Rooms</p>

  <div class="credits">
    <p>Directed by Lyle and Marjorie Fenstrom</p>
    <p>Rosa Quillmane Dorsk, Resident Choreographer</p>
  </div>

  <div class="studio-mark">
    <span class="dot"></span>
    <span class="name">HDT Studio for Movement Learning</span>
  </div>

  <div class="contact">
    <p class="phone">555-318-7042</p>
    <p>www.pelburydancetheatre.example</p>
  </div>
</main>
</body>
</html>
```